Real Estate Renovation and Rental:Business Card/Logo Design Project

Brackwell Holdings LLC is a small partnership that buys homes to renovate, then provide as rentals to people who may not currently be able to purchase a home - but we also coach them on how to improve their credit so that, in 2-5 years, they may be able to buy a home. Maybe even the one they're living in.

We are based in Sonoma County of Northern California, operating in communities including Healdsburg, Windsor, Santa Rosa, and Cloverdale.

Please design a business card, but the same logo should work for signs that we will post on the homes as they are being renovated.

The design should be clean, contemporary, professional but warm. I'd love to see a rooftop feature, or some other element of a house. Again, not too much detail, clean and welcoming. The design must include "Brackwell Holdings LLC" - but "BHLLC" could also be used as a primary name, with "Brackwell Holdings LLC" in smaller print somewhere. If using "BHLLC", the BH could be visually distinct (larger, different color, font) than the LLC part of the name but they must be together.
Updates

just conferring with partner to choose a final design ... should be ready to choose soon and will post

Industry/Entity Type

Business

Requirements
Must have
• the name "Brackwell Holdings LLC"
for business card design, and leave room for us to customize with partner names, address, telephone numbers, email addresses
Nice to have
• some element of a house included

```html
<!DOCTYPE html>
<html lang="en">
<head>
<meta charset="utf-8">
<title>Brackwell Holdings LLC – Business Card</title>
<link rel="stylesheet" href="https://fonts.googleapis.com/css2?family=Montserrat:wght@400;600;700&display=swap">
<style>
  :root {
    --backdrop: #e4e5e7;
    --card: #ffffff;
    --ink-dark: #3b3d40;
    --ink-mid: #55575a;
    --brand-blue: #2d6e92;
  }
  * { margin: 0; padding: 0; box-sizing: border-box; }
  html, body {
    width: 1200px;
    height: 1000px;
    overflow: hidden;
    background: var(--backdrop);
    font-family: "Montserrat", "Century Gothic", sans-serif;
  }
  .business-card {
    position: absolute;
    left: 75px;
    top: 200px;
    width: 1050px;
    height: 600px;
    background: var(--card);
    box-shadow: 0 12px 40px rgba(0,0,0,0.12);
    overflow: hidden;
  }
  .holder-name {
    position: absolute;
    left: 60px;
    top: 62px;
    font-size: 42px;
    line-height: 1.2;
    font-weight: 700;
    letter-spacing: 1.5px;
    text-transform: uppercase;
    color: var(--ink-dark);
  }
  .holder-title {
    position: absolute;
    left: 62px;
    top: 118px;
    font-size: 26px;
    line-height: 1.3;
    font-weight: 400;
    color: var(--ink-mid);
  }
  .contact-list {
    position: absolute;
    left: 62px;
    top: 180px;
    list-style: none;
    font-size: 25px;
    line-height: 40px;
    color: var(--ink-mid);
  }
  .contact-label {
    font-weight: 700;
    color: var(--ink-dark);
  }
  .address {
    position: absolute;
    left: 120px;
    top: 370px;
    font-style: normal;
    font-size: 25px;
    line-height: 38px;
    color: var(--ink-mid);
  }
  .base-rule {
    position: absolute;
    left: 0;
    top: 488px;
    width: 600px;
    height: 11px;
    background: var(--brand-blue);
  }
  .brand-mark {
    position: absolute;
    right: 60px;
    top: 360px;
    height: 110px;
    display: flex;
    align-items: center;
    gap: 18px;
  }
  .brand-mark svg { display: block; }
  .brand-mark-text {
    font-size: 96px;
    line-height: 1;
    font-weight: 700;
    color: var(--brand-blue);
    letter-spacing: 2px;
  }
  .company-name {
    position: absolute;
    right: 60px;
    top: 518px;
    font-size: 32px;
    line-height: 1;
    font-weight: 700;
    letter-spacing: 1px;
    text-transform: uppercase;
    color: var(--brand-blue);
  }
</style>
</head>
<body>
  <article class="business-card">
    <h1 class="holder-name">Dana Whitfield</h1>
    <p class="holder-title">Sales Director</p>
    <ul class="contact-list">
      <li><span class="contact-label">Office:</span> +1 707 555 0142</li>
      <li><span class="contact-label">Mobile:</span> +1 707 555 0187</li>
      <li><span class="contact-label">Email:</span> dana@brackwellholdings.com</li>
      <li><span class="contact-label">Web:</span> www.brackwellholdings.com</li>
    </ul>
    <address class="address">
      Address line 1<br>
      Address line 2
    </address>
    <div class="base-rule"></div>
    <div class="brand-mark">
      <svg width="40" height="40" viewBox="0 0 40 40" aria-hidden="true">
        <rect width="40" height="40" fill="#2d6e92"/>
      </svg>
      <span class="brand-mark-text">BHLLC</span>
    </div>
    <p class="company-name">Brackwell Holdings LLC</p>
  </article>
</body>
</html>
```